Brightmoor Partners Branding Revamp

We are a consulting company, looking for a way to display and promote our brand. We have 2 sides to the business- Brightmoor (financial) and Partners (cyber security). The financial side products relate to business necessities: card processing, website design/hosting/maintenance, VoIP phone systems. The cyber security side promotes a bundled package of 4 solutions: network vulnerability scan, dark web scan, anti-ransomeware/malware software, and image-level backups. We want people to understand that partnering with Brightmoor Partners gives them “Elevated Peace of Mind” (tagline). Current badge and logos uploaded.

Target Market(s)

Small businesses

Contact Information for Business Card

Lena Marwick, Vice President, lena@brightmoorpartners.example, 555-806-1937, www.brightmoorpartners.example

Requirements
Nice to have
• I do prefer the darker background for front and back

```html
<!DOCTYPE html>
<html lang="en">
<head>
<meta charset="utf-8">
<title>Brightmoor Partners – Business Card</title>
<link rel="stylesheet" href="https://fonts.googleapis.com/css2?family=Montserrat:wght@400;500;600&display=swap">
<style>
  :root{
    --stage:#2a2a2c;
    --card:#1b1b1d;
    --red:#ec1c24;
    --white:#ffffff;
    --muted:#e9e9e9;
  }
  *{margin:0;padding:0;box-sizing:border-box}
  html,body{width:1200px;height:881px;overflow:hidden}
  body{
    background:var(--stage);
    font-family:"Montserrat",Arial,sans-serif;
    display:flex;align-items:center;justify-content:center;gap:40px;
  }
  .card{
    position:relative;width:540px;height:309px;background:var(--card);
    overflow:hidden;box-shadow:0 12px 30px rgba(0,0,0,.45);
  }
  .card--back{display:flex;align-items:center;justify-content:center}
  .wordmark{display:flex;align-items:center;gap:14px}
  .wordmark__dot{width:16px;height:16px;background:var(--red)}
  .wordmark__name{
    color:var(--white);font-weight:600;letter-spacing:.32em;
    text-transform:uppercase;font-size:22px;white-space:nowrap;
  }
  .card--front .wordmark{position:absolute;left:30px;top:46px;gap:10px}
  .card--front .wordmark__dot{width:10px;height:10px}
  .card--front .wordmark__name{font-size:13px;letter-spacing:.3em}
  .accent-bar{position:absolute;left:24px;top:128px;width:6px;height:40px;background:var(--red)}
  .person{position:absolute;left:44px;top:122px}
  .person__name{color:var(--red);font-size:26px;font-weight:500;text-transform:uppercase;letter-spacing:.01em;line-height:1;white-space:nowrap}
  .person__role{color:var(--muted);font-size:14px;text-transform:uppercase;margin-top:6px;letter-spacing:.03em}
  .divider{width:30px;height:2px;background:var(--red);margin:12px 0 12px}
  .contacts{list-style:none}
  .contacts li{display:flex;align-items:center;gap:9px;color:var(--white);font-size:14px;line-height:22px;white-space:nowrap}
  .contacts svg{width:12px;height:12px;flex:none}
  .bottom-band{position:absolute;left:0;right:0;bottom:0;height:22px;background:var(--red)}
</style>
</head>
<body>

  <section class="card card--back" aria-label="Card back">
    <div class="wordmark">
      <span class="wordmark__dot"></span>
      <span class="wordmark__name">Brightmoor Partners</span>
    </div>
  </section>

  <section class="card card--front" aria-label="Card front">
    <div class="wordmark">
      <span class="wordmark__dot"></span>
      <span class="wordmark__name">Brightmoor Partners</span>
    </div>

    <span class="accent-bar"></span>
    <div class="person">
      <p class="person__name">Lena Marwick</p>
      <p class="person__role">Vice President</p>
      <div class="divider"></div>
      <ul class="contacts">
        <li>
          <svg viewBox="0 0 12 12" aria-hidden="true"><path d="M2.5 1h2l1 3-1.3 1a6 6 0 0 0 2.8 2.8l1-1.3 3 1v2a1 1 0 0 1-1 1A9.5 9.5 0 0 1 1.5 2a1 1 0 0 1 1-1z" fill="var(--red)"/></svg>
          +1 555-806-1937
        </li>
        <li>
          <svg viewBox="0 0 12 12" aria-hidden="true"><rect x="1" y="2.5" width="10" height="7" fill="none" stroke="var(--red)" stroke-width="1.2"/><path d="M1 2.5l5 4 5-4" fill="none" stroke="var(--red)" stroke-width="1.2"/></svg>
          lena@brightmoorpartners.example
        </li>
        <li>
          <svg viewBox="0 0 12 12" aria-hidden="true"><circle cx="6" cy="6" r="5" fill="none" stroke="var(--red)" stroke-width="1.1"/><ellipse cx="6" cy="6" rx="2.2" ry="5" fill="none" stroke="var(--red)" stroke-width="1"/><path d="M1 6h10" stroke="var(--red)" stroke-width="1"/></svg>
          www.brightmoorpartners.example
        </li>
      </ul>
    </div>

    <span class="bottom-band"></span>
  </section>

</body>
</html>
```